Web design for a food truck business

We need a web design for an established food truck business who have an active Facebook following but no website. We are a digital marketing agency and the client is looking for a website that stands out and doesn't have a corporate or boring look to it.
The client's facebook page is: https://www.facebook.com/DonTamalVivoz/

Number of Pages Required

1 page

```html
<!DOCTYPE html>
<html lang="en">
<head>
<meta charset="utf-8">
<title>Dulce Rueda — Churro Food Truck</title>
<link rel="stylesheet" href="https://fonts.googleapis.com/css2?family=Raleway:wght@400;600;700&family=Open+Sans:wght@400;600;700&display=swap">
<style>
  :root {
    --ink: #333333;
    --muted: #666666;
    --beige: #e9dcc0;
    --gold: #f1c94b;
    --red: #b8322a;
    --footer: #222222;
    --footer-line: #3a3a3a;
    --footer-text: #bdbdbd;
    --white: #ffffff;
  }
  * { margin: 0; padding: 0; box-sizing: border-box; }
  html, body { width: 1200px; height: 2720px; overflow: hidden; }
  body {
    position: relative;
    background: var(--white);
    font-family: "Open Sans", Arial, sans-serif;
    color: var(--ink);
  }
  .hero {
    position: absolute; left: 0; top: 0; width: 1200px; height: 560px;
    background:
      radial-gradient(ellipse 260px 90px at 330px 170px, rgba(214,150,72,.85), rgba(214,150,72,0)),
      radial-gradient(ellipse 300px 110px at 860px 300px, rgba(205,140,62,.85), rgba(205,140,62,0)),
      radial-gradient(ellipse 240px 80px at 520px 420px, rgba(196,128,55,.8), rgba(196,128,55,0)),
      radial-gradient(ellipse 200px 70px at 1040px 130px, rgba(210,146,70,.75), rgba(210,146,70,0)),
      linear-gradient(180deg, #8a7458 0%, #a58d6c 50%, #7c6650 100%);
  }
  .main-nav {
    position: absolute; left: 0; top: 0; width: 1200px; height: 96px;
    background: linear-gradient(rgba(0,0,0,.6), rgba(0,0,0,0));
  }
  .main-nav a {
    position: absolute; top: 32px; color: var(--white); text-decoration: none;
    font-size: 16px; font-weight: 600;
  }
  .brand {
    position: absolute; left: 520px; top: 0; width: 168px; height: 180px;
    background: var(--gold); display: flex; align-items: center; justify-content: center; gap: 10px;
  }
  .brand-dot { width: 18px; height: 18px; border-radius: 50%; background: var(--red); }
  .brand-name {
    font-family: "Raleway", Arial, sans-serif; font-weight: 700; font-size: 24px;
    color: var(--red); line-height: 1.1; text-align: center;
  }
  .events {
    position: absolute; left: 0; top: 560px; width: 1200px; height: 488px; background: var(--beige);
  }
  .truck-art {
    position: absolute; left: 128px; top: 68px; width: 432px; height: 192px;
    background:
      radial-gradient(ellipse 120px 60px at 220px 90px, rgba(255,255,255,.55), rgba(255,255,255,0)),
      linear-gradient(180deg, #8fb7bf 0%, #5f8f9a 70%, #3d4f55 100%);
    border-radius: 20px 70px 12px 12px;
  }
  .events-copy { position: absolute; left: 620px; top: 100px; width: 470px; }
  .events-copy h2 {
    font-family: "Raleway", Arial, sans-serif; font-weight: 600; font-size: 22px; line-height: 1.35; margin-bottom: 20px;
  }
  .events-copy p { font-size: 13px; line-height: 1.8; color: var(--muted); }
  .section-title {
    position: absolute; left: 0; width: 1200px; text-align: center;
    font-family: "Raleway", Arial, sans-serif; font-weight: 600; font-size: 26px; letter-spacing: 1px; color: var(--ink);
  }
  .gallery-grid {
    position: absolute; left: 0; top: 1104px; width: 584px; height: 456px;
    display: grid; grid-template-columns: repeat(3, 1fr); grid-template-rows: repeat(4, 1fr); gap: 4px;
  }
  .gallery-grid div { background: radial-gradient(circle at 40% 45%, #f4e6c8, #c98a4a 55%, #6f4a2c); }
  .gallery-grid div:nth-child(3n+2) { background: radial-gradient(circle at 50% 50%, #ffffff, #c9d79a 45%, #7a8f3e); }
  .gallery-grid div:nth-child(4n) { background: radial-gradient(circle at 50% 50%, #fbeee0, #d56a48 55%, #7e2a1c); }
  .gallery-grid div:nth-child(5n+1) { background: radial-gradient(circle at 50% 50%, #f7f1e8, #e1b77a 50%, #8a5a30); }
  .gallery-feature {
    position: absolute; left: 588px; top: 1104px; width: 612px; height: 456px;
    background:
      radial-gradient(circle at 20% 25%, #f6c25a, rgba(246,194,90,0) 22%),
      radial-gradient(circle at 60% 35%, #f4bb50, rgba(244,187,80,0) 20%),
      radial-gradient(circle at 35% 70%, #f2b84c, rgba(242,184,76,0) 22%),
      radial-gradient(circle at 80% 75%, #f5c058, rgba(245,192,88,0) 20%),
      linear-gradient(135deg, #c98a38, #a8661e);
  }
  .testimonials { position: absolute; left: 128px; top: 1790px; width: 500px; }
  .quote { font-size: 12px; line-height: 1.65; color: var(--muted); }
  .quote-mark { color: var(--ink); font-weight: 700; margin-right: 4px; }
  .quote-author { font-size: 12px; color: var(--muted); margin: 14px 0 18px; }
  .clients-art {
    position: absolute; left: 660px; top: 1760px; width: 460px; height: 460px;
    background:
      radial-gradient(ellipse 200px 230px at 230px 270px, #c9d6e6, rgba(201,214,230,0)),
      radial-gradient(ellipse 120px 160px at 80px 320px, #d9c2ad, rgba(217,194,173,0)),
      radial-gradient(ellipse 120px 160px at 390px 320px, #c8b49e, rgba(200,180,158,0)),
      linear-gradient(180deg, #ffffff 0%, #e8ecf1 40%, #9fb4cc 100%);
  }
  .site-footer {
    position: absolute; left: 0; top: 2220px; width: 1200px; height: 500px; background: var(--footer); color: var(--footer-text);
  }
  .footer-col { position: absolute; top: 66px; }
  .footer-col h3 {
    font-family: "Raleway", Arial, sans-serif; font-size: 14px; font-weight: 700; color: var(--white);
    text-transform: uppercase; letter-spacing: .5px; margin-bottom: 20px;
  }
  .footer-col p { font-size: 12px; line-height: 1.8; }
  .hours { width: 290px; border-collapse: collapse; font-size: 12px; }
  .hours td { padding: 5px 0; border-bottom: 1px solid var(--footer-line); }
  .hours td:first-child { color: var(--white); font-weight: 600; }
  .hours td:last-child { text-align: right; }
  .contact-line { font-size: 12px; line-height: 1.6; margin-bottom: 12px; }
  .contact-line strong { color: var(--white); font-weight: 600; display: block; }
  .social { display: flex; gap: 8px; margin-top: 6px; }
  .social span { width: 24px; height: 24px; background: var(--white); border-radius: 3px; }
  .footer-bottom {
    position: absolute; left: 128px; top: 420px; width: 944px; padding-top: 18px;
    border-top: 1px solid var(--footer-line); font-size: 12px; display: flex; justify-content: space-between;
  }
  .footer-bottom nav a { color: var(--footer-text); text-decoration: none; margin-left: 30px; }
</style>
</head>
<body>
  <header class="hero" role="img" aria-label="Close-up photograph of fresh sugared churros">
    <nav class="main-nav">
      <a href="#" style="left:186px">Home</a>
      <a href="#" style="left:280px">Menu</a>
      <a href="#" style="left:370px">Truck locator</a>
      <a href="#" style="left:738px">Events</a>
      <a href="#" style="left:840px">News</a>
      <a href="#" style="left:928px">Contact</a>
    </nav>
    <div class="brand"><span class="brand-dot"></span><span class="brand-name">Dulce<br>Rueda</span></div>
  </header>

  <section class="events">
    <div class="truck-art" role="img" aria-label="Illustration of the blue churro food truck"></div>
    <div class="events-copy">
      <h2>Do you want Dulce Rueda at your<br>next event?</h2>
      <p>We cater birthdays, work events, weddings and everything in between! Just send us an email at hola@dulcerueda.example for a quote! We cater all types of events. Birthdays, weddings, work functions and everything in between! Contact us for a quote: events@dulcerueda.example. Special discounts offered for events in July &amp; August!</p>
    </div>
  </section>

  <h2 class="section-title" style="top:1040px">OUR GALLERY</h2>
  <div class="gallery-grid" role="img" aria-label="Grid of food photographs">
    <div></div><div></div><div></div><div></div><div></div><div></div>
    <div></div><div></div><div></div><div></div><div></div><div></div>
  </div>
  <div class="gallery-feature" role="img" aria-label="Photograph of a tray of golden star-shaped churros"></div>

  <h2 class="section-title" style="top:1636px">WHAT OUR CLIENTS TO SAY ?</h2>
  <section class="testimonials">
    <p class="quote"><span class="quote-mark">&#8220;</span>Lorem ipsum dolor sit amet, consectetur adipisicing elit, sed do eiusmod tempor incididunt ut labore et dolore magna aliqua. Ut enim ad minim veniam, quis nostrud exercitation ullamco laboris nisi ut aliquip ex ea commodo consequat.</p>
    <p class="quote-author">Alicia</p>
    <p class="quote"><span class="quote-mark">&#8220;</span>Lorem ipsum dolor sit amet, consectetur adipisicing elit, sed do eiusmod tempor incididunt ut labore et dolore magna aliqua. Ut enim ad minim veniam, quis nostrud exercitation ullamco laboris nisi ut aliquip ex ea commodo consequat.</p>
    <p class="quote-author">Marissa</p>
    <p class="quote"><span class="quote-mark">&#8220;</span>Lorem ipsum dolor sit amet, consectetur adipisicing elit, sed do eiusmod tempor incididunt ut labore et dolore magna aliqua. Ut enim ad minim veniam, quis nostrud exercitation ullamco laboris nisi ut aliquip ex ea commodo consequat.</p>
    <p class="quote-author">Tom</p>
  </section>
  <div class="clients-art" role="img" aria-label="Photograph of a group of happy customers"></div>

  <footer class="site-footer">
    <div class="footer-col" style="left:144px;width:280px">
      <h3>About Dulce Rueda</h3>
      <p>We are a family-run food truck serving fresh, hot churros across the city. Find us at markets, festivals and private events all year round, rain or shine.</p>
    </div>
    <div class="footer-col" style="left:480px">
      <h3>Opening Hours</h3>
      <table class="hours">
        <tr><td>Monday</td><td>8:00 AM – 5:00 PM</td></tr>
        <tr><td>Tuesday</td><td>8:00 AM – 5:00 PM</td></tr>
        <tr><td>Wednesday</td><td>8:00 AM – 5:00 PM</td></tr>
        <tr><td>Thursday</td><td>8:00 AM – 5:00 PM</td></tr>
        <tr><td>Friday</td><td>8:00 AM – 5:00 PM</td></tr>
        <tr><td>Saturday</td><td>8:00 AM – 5:00 PM</td></tr>
        <tr><td>Sunday</td><td>Closed</td></tr>
      </table>
    </div>
    <div class="footer-col" style="left:820px">
      <h3>Connect With Us</h3>
      <p class="contact-line"><strong>Catering</strong>(043) 555 0170</p>
      <p class="contact-line"><strong>Office</strong>(043) 555 0188</p>
      <div class="social"><span></span><span></span><span></span><span></span><span></span></div>
    </div>
    <div class="footer-bottom">
      <span>2017 All Rights Reserved</span>
      <nav><a href="#">Home</a><a href="#">Lunch Menu</a><a href="#">Truck Locator</a><a href="#">News</a><a href="#">Contact</a></nav>
    </div>
  </footer>
</body>
</html>
```